Business Cards Needed for Innovative Healthcare Marketing Company

We are a marketing company focused on healthcare. Our company is all about rebranding yourself renewing your image and generating results. The phoenix stands for "reborn" or "rising" which we provide new brands for our clients we take their old brands and renew it with creativity and innovation. I am looking for a business card with color dimension. I have attached an example of a card I think has the look and feel of what I am trying to accomplish. I like that the card example has black and grey font colors, I like the font placement and the small logo, I really like the use of the colors on the right those are the colors of my logo. My logo is phoenix so maybe incorporating flames similar to that design. I would like the back a solid color maybe red with an opaque version of the logo and website. As a marketing company I am always open to creative liberty!

Target Market(s)

Doctors and business professionals.

Industry/Entity Type

Marketing

Contact Information for Business Card

Vornaly Health Care Marketing
Marnie Okonski- CEO
#(502)638-2947
email-marnie@vornaly.com
website- vornaly.com

Font styles to use
Sans Serif

Colors
ec1f27
f37122
ffc214
fbed22
fbf289
f04a50

Requirements
Must have
• The logo and required information
Nice to have
• icons by the information
Should not have
• child like font

```html
<!DOCTYPE html>
<html lang="en">
<head>
<meta charset="utf-8">
<title>Vornaly Health Care Marketing – Business Card</title>
<link rel="stylesheet" href="https://fonts.googleapis.com/css2?family=Arimo:wght@400;700&display=swap">
<style>
  :root {
    --red-deep: #ec1f27;
    --red-card: #ee3640;
    --red-soft: #f04a50;
    --orange: #f37122;
    --amber: #ffc214;
    --yellow: #fbed22;
    --yellow-pale: #fbf289;
    --ink-grey: #5a5a5a;
    --ink-dark: #4a3a3a;
    --icon-maroon: #8a1c1c;
    --page: #ffffff;
  }
  * { box-sizing: border-box; margin: 0; padding: 0; }
  html, body {
    width: 1200px; height: 1200px; overflow: hidden;
    background: var(--page);
    font-family: "Arimo", Arial, sans-serif;
  }
  .card {
    position: absolute; left: 222px;
    width: 756px; height: 431px; overflow: hidden;
  }

  /* ---------- back side ---------- */
  .card-back { top: 105px; background: var(--red-card); }
  .card-back .light-beams { position: absolute; inset: 0; }
  .card-back .brand-mark {
    position: absolute; left: 50%; top: 62px; transform: translateX(-50%);
    width: 120px; height: 120px; border-radius: 50%;
    background: linear-gradient(180deg, var(--red-deep), var(--orange));
    opacity: .55;
  }
  .card-back .brand-name {
    position: absolute; left: 0; right: 0; top: 212px;
    text-align: center; font-weight: 400; font-size: 34px; letter-spacing: 1px;
    color: var(--ink-dark); opacity: .8; line-height: 1.15;
  }
  .card-back .web-band {
    position: absolute; left: 0; right: 0; bottom: 0; height: 53px;
    background: var(--red-deep);
  }
  .card-back .web-address {
    position: absolute; left: 0; right: 0; bottom: 10px;
    text-align: center; font-weight: 700; font-size: 37px;
    color: var(--orange); letter-spacing: .5px;
  }

  /* ---------- front side ---------- */
  .card-front { top: 665px; background: var(--yellow-pale); }
  .card-front .flame-curves { position: absolute; inset: 0; }
  .card-front .brand {
    position: absolute; left: 18px; top: 22px;
    display: flex; align-items: center; gap: 14px;
  }
  .card-front .brand-mark {
    width: 90px; height: 90px; border-radius: 50%;
    background: linear-gradient(180deg, var(--red-deep), var(--amber));
  }
  .card-front .brand-name {
    font-weight: 400; font-size: 25px; line-height: 1.2;
    color: var(--ink-dark); width: 190px;
  }
  .card-front .person-name {
    position: absolute; left: 33px; top: 160px;
    font-weight: 700; font-size: 36px; color: var(--orange);
  }
  .card-front .person-title {
    position: absolute; left: 127px; top: 203px;
    font-weight: 700; font-size: 29px; color: var(--ink-grey);
  }
  .contact-list { position: absolute; left: 22px; top: 257px; list-style: none; }
  .contact-item {
    display: flex; align-items: center; gap: 22px;
    height: 33px; margin-bottom: 21px;
    font-weight: 700; font-size: 25px; color: var(--ink-grey);
  }
  .contact-icon { width: 33px; height: 33px; flex: none; }
</style>
</head>
<body>

<section class="card card-back" aria-label="Card back">
  <svg class="light-beams" viewBox="0 0 756 431" aria-hidden="true">
    <polygon points="60,0 140,0 330,431 250,431" fill="#ffffff" opacity=".06"/>
    <polygon points="616,0 696,0 506,431 426,431" fill="#ffffff" opacity=".06"/>
  </svg>
  <div class="brand-mark" aria-hidden="true"></div>
  <p class="brand-name">VORNALY<br>HEALTH CARE MARKETING</p>
  <div class="web-band"></div>
  <p class="web-address">www.vornaly.com</p>
</section>

<section class="card card-front" aria-label="Card front">
  <svg class="flame-curves" viewBox="0 0 756 431" aria-hidden="true">
    <path d="M360,0 C345,120 480,205 756,210 L756,0 Z" fill="var(--amber)"/>
    <path d="M392,0 C385,110 520,182 756,182 L756,0 Z" fill="var(--yellow)"/>
    <path d="M405,431 C405,320 530,215 756,212 L756,431 Z" fill="var(--amber)"/>
    <path d="M445,431 C452,330 565,238 756,226 L756,431 Z" fill="var(--orange)"/>
    <path d="M470,178 C560,218 680,218 756,206 L756,262 C650,244 540,232 470,178 Z" fill="var(--red-soft)" opacity=".55"/>
  </svg>

  <div class="brand">
    <div class="brand-mark" aria-hidden="true"></div>
    <p class="brand-name">VORNALY<br>HEALTH CARE MARKETING</p>
  </div>

  <h1 class="person-name">Marnie Okonski</h1>
  <p class="person-title">CEO</p>

  <ul class="contact-list">
    <li class="contact-item">
      <svg class="contact-icon" viewBox="0 0 33 33" aria-hidden="true">
        <rect width="33" height="33" fill="#ffffff"/>
        <path d="M10,8 L14,8 L15.5,13 L13,15 C14,18 16,20 19,21 L21,18.5 L26,20 L26,24 C26,25 25,26 24,26 C15,25 9,19 8,10 C8,9 9,8 10,8 Z" fill="#333"/>
      </svg>
      <span>(502)638-2947</span>
    </li>
    <li class="contact-item">
      <svg class="contact-icon" viewBox="0 0 33 33" aria-hidden="true">
        <rect width="33" height="33" fill="var(--icon-maroon)"/>
        <path d="M10,8 L25,15 L18.5,17 L22,24 L19.5,25.2 L16,18.3 L11,22 Z" fill="#ffffff"/>
      </svg>
      <span>marnie@vornaly.com</span>
    </li>
    <li class="contact-item">
      <svg class="contact-icon" viewBox="0 0 33 33" aria-hidden="true">
        <rect width="33" height="33" fill="#ffffff"/>
        <circle cx="16.5" cy="16.5" r="10" fill="#333"/>
        <g stroke="#ffffff" stroke-width="1.3" fill="none">
          <ellipse cx="16.5" cy="16.5" rx="4.5" ry="10"/>
          <line x1="6.5" y1="16.5" x2="26.5" y2="16.5"/>
          <line x1="8" y1="11.5" x2="25" y2="11.5"/>
          <line x1="8" y1="21.5" x2="25" y2="21.5"/>
        </g>
      </svg>
      <span>www.vornaly.com</span>
    </li>
  </ul>
</section>

</body>
</html>
```